Design Business Card MAPLE WREN MOWING

We have attached a copy of our Logo, we like a business card designed with logo and mobile phone number on one side that stands out maybe gloss and on the other side it can have the services we do small picture of our logo name number, I have attached an idea to this that I have seen online, this is a business owned by a woman so we like pinks black and navy
Our logo is attached in pdf
Target Market(s)
Home owners that need lawns mowed
Industry/Entity Type
Lawns and gardens
Contact Information for Business Card
Logo business Owner name Deborah Finch mobile number 0491627504
Font styles to use
Look and feel
Each slider illustrates characteristics of the customer's brand and the style your logo design should communicate.

```html
<!DOCTYPE html>
<html lang="en">
<head>
<meta charset="utf-8">
<title>Maple Wren Mowing – Business Card</title>
<link href="https://fonts.googleapis.com/css2?family=Russo+One&family=Exo+2:ital,wght@0,800;1,800;1,900&display=swap" rel="stylesheet">
<style>
  :root {
    --page: #e9ece9;
    --ink: #0b0b0b;
    --card-dark: #050505;
    --card-dark-sheen: #3a3a3a;
    --card-light: #ffffff;
    --pink: #e0459e;
    --pink-deep: #b82c7c;
    --grass-light: #b8dc4a;
    --grass-mid: #6ccf3c;
    --grass-deep: #2fb04f;
  }
  * { box-sizing: border-box; margin: 0; padding: 0; }
  html, body { width: 1200px; height: 900px; overflow: hidden; }
  body {
    background: var(--page);
    display: flex;
    flex-direction: column;
    align-items: center;
    justify-content: center;
    gap: 36px;
    font-family: "Exo 2", sans-serif;
  }
  .card {
    position: relative;
    width: 720px;
    height: 405px;
    overflow: hidden;
    box-shadow: 0 6px 18px rgba(0,0,0,.18);
  }

  /* Front */
  .card--front {
    background: linear-gradient(100deg, var(--card-dark) 0%, var(--card-dark) 62%, var(--card-dark-sheen) 63%, #151515 100%);
  }
  .brand {
    position: absolute;
    font-family: "Russo One", sans-serif;
    color: var(--pink);
    text-transform: uppercase;
  }
  .card--front .brand {
    left: 0; right: 0; top: 140px;
    display: flex;
    align-items: center;
    justify-content: center;
    gap: 14px;
    font-size: 46px;
    white-space: nowrap;
  }
  .brand__mark {
    width: 26px; height: 26px;
    border-radius: 50%;
    background: var(--pink);
    flex: none;
  }
  .grass-band {
    position: absolute;
    left: 0; right: 0; bottom: 0;
    background: linear-gradient(180deg, rgba(184,220,74,0) 0%, var(--grass-light) 35%, var(--grass-mid) 70%, var(--grass-deep) 100%);
  }
  .card--front .grass-band { height: 92px; }

  /* Back */
  .card--back { background: var(--card-light); }
  .card--back .grass-band { height: 165px; }
  .mower-art {
    position: absolute;
    left: 40px; top: 18px;
    width: 335px; height: 290px;
    border-radius: 18px;
    background: radial-gradient(ellipse at 55% 60%, var(--pink) 0%, #c64d93 40%, #2a2a2a 100%);
    opacity: .9;
  }
  .card--back .brand {
    left: 400px; top: 50px;
    width: 290px;
    font-size: 38px;
    line-height: 1.05;
    text-align: center;
  }
  .brand__line { display: block; white-space: nowrap; }
  .owner {
    position: absolute;
    left: 395px; top: 185px;
    display: inline-flex;
    flex-direction: column;
    align-items: flex-end;
  }
  .owner__name {
    font-weight: 900;
    font-style: italic;
    font-size: 30px;
    color: var(--pink);
    letter-spacing: 1px;
    text-transform: uppercase;
    white-space: nowrap;
  }
  .owner__role {
    font-weight: 800;
    font-style: italic;
    font-size: 19px;
    color: var(--ink);
    margin-top: 2px;
  }
  .contact {
    position: absolute;
    left: 150px; bottom: 30px;
    display: flex;
    align-items: center;
    gap: 18px;
  }
  .contact__icon { width: 46px; height: 46px; flex: none; }
  .contact__phone {
    font-weight: 900;
    font-style: italic;
    font-size: 50px;
    color: var(--ink);
    letter-spacing: 2px;
    white-space: nowrap;
  }
</style>
</head>
<body>

  <section class="card card--front" aria-label="Business card front">
    <div class="brand"><span class="brand__mark"></span>Maple Wren Mowing</div>
    <div class="grass-band" role="img" aria-label="Illustrated green grass border"></div>
  </section>

  <section class="card card--back" aria-label="Business card back">
    <div class="grass-band" role="img" aria-label="Illustrated green grass border"></div>
    <div class="mower-art" role="img" aria-label="Illustration of a pink and black push lawn mower on grass"></div>
    <div class="brand"><span class="brand__line">Maple Wren</span><span class="brand__line">Mowing</span></div>
    <div class="owner">
      <p class="owner__name">Deborah Finch</p>
      <p class="owner__role">Owner</p>
    </div>
    <div class="contact">
      <svg class="contact__icon" viewBox="0 0 46 46" aria-hidden="true">
        <circle cx="23" cy="23" r="23" fill="#0b0b0b"/>
        <path d="M15 13c1.5-1 3-.5 3.8 1l1.8 3.4c.6 1.2.3 2.4-.7 3.1l-1.3 1c1.1 2.6 3.2 4.8 5.9 6l1-1.3c.7-1 2-1.3 3.1-.7l3.4 1.8c1.5.8 2 2.3 1 3.8-1.2 1.8-3.4 2.8-5.6 2.2-7-1.9-12.5-7.4-14.4-14.4-.6-2.2.4-4.4 2-5.9z" fill="#fff"/>
      </svg>
      <span class="contact__phone">0491627504</span>
    </div>
  </section>

</body>
</html>
```